Psychotherapist's business card

I need a business card design for a psychotherapist. I expect business card to have "light" design. By this I mean that it can somehow translate easiness, serenity. Maybe pastel colours can help you here. I have attached some pictures from Greece. Perhaps they can inspire you to combine colours and to achieve that "light" design.
Updates

Pls, don't use any free samples you may find on business card generators. It looks too simple, uncreative and waste of time! READ size and colour requirements! I don't want to see any shapes like rings, triangles etc.

Contact Information for Business Card

Size: 65mmX60mm

Name - Вячеслав Мирошенко

Психолог
+7(916)482-30-67
miroshenko.com

I suppose that thin font can look good but it's up to you

Requirements
Must have
• size requirements
Nice to have
• pastel colours
• thin font
Should not have
• black and dark colours
• lines, free design samples used from other web-sites

```html
<!DOCTYPE html>
<html lang="ru">
<head>
<meta charset="utf-8">
<title>Вячеслав Мирошенко — визитка</title>
<link href="https://fonts.googleapis.com/css2?family=PT+Serif:wght@400&display=swap" rel="stylesheet">
<style>
  :root {
    --backdrop: #aad9dc;
    --card: #ffffff;
    --sun-yellow: #f6ef6c;
    --blush: #fac9bb;
    --aqua-dots: #bfe9ec;
    --ink-blue: #1d5a9c;
  }
  html, body {
    margin: 0;
    width: 1200px;
    height: 1200px;
    overflow: hidden;
    background: var(--backdrop);
  }
  .business-card {
    position: absolute;
    left: 50px;
    top: 228px;
    width: 1100px;
    height: 744px;
    background: var(--card);
    overflow: hidden;
    font-family: "PT Serif", Georgia, serif;
    color: var(--ink-blue);
  }
  .block { position: absolute; }
  .block--yellow { left: 0; top: 0; width: 857px; height: 186px; background: var(--sun-yellow); }
  .block--dots-top { left: 610px; top: 88px; width: 490px; height: 145px; background: var(--aqua-dots); }
  .block--blush { left: 604px; top: 556px; width: 496px; height: 188px; background: var(--blush); }
  .block--dots-bottom { left: 0; top: 651px; width: 726px; height: 93px; background: var(--aqua-dots); }

  .identity { position: absolute; left: 55px; top: 250px; }
  .identity__name {
    margin: 0;
    font-size: 43px;
    font-weight: 400;
    letter-spacing: 1px;
    word-spacing: 8px;
    line-height: 50px;
  }
  .identity__role { margin: 0; font-size: 30px; line-height: 36px; }

  .contacts {
    position: absolute;
    left: 55px;
    top: 422px;
    margin: 0;
    padding: 0;
    list-style: none;
    font-size: 30px;
    line-height: 40px;
  }
</style>
</head>
<body>
  <article class="business-card">
    <div class="block block--yellow"></div>
    <div class="block block--dots-top" role="img" aria-label="Поле голубого точечного узора"></div>
    <div class="block block--blush"></div>
    <div class="block block--dots-bottom" role="img" aria-label="Полоса голубого точечного узора"></div>

    <header class="identity">
      <h1 class="identity__name">Вячеслав Мирошенко</h1>
      <p class="identity__role">psychotherapist.</p>
    </header>

    <ul class="contacts">
      <li class="contacts__title">Психолог</li>
      <li class="contacts__phone">+7(916)482-30-67</li>
      <li class="contacts__site">miroshenko.com</li>
    </ul>
  </article>
</body>
</html>
```